Morden, Creative, Unique, Independent Wine Shop

1. We are a brand new wine shop located in Melbourne Australia, we have our logo already, simply use the logo to design a business card.
2. I have uploaded our logo in two versions, with or without shadow, any of them is acceptable.
3. Make it as creative and unique as possible, no limitation of shape, color combination, geometry pattern, fonts, composing etc.
3. Info on the card:
- Brambleford Wine Cellar (Not very necessary if logo is obviously shown)
- 42 Ferncastle Steet, Alderbrook, Wynmoor, Australia 3999
- +61 3 9018 4637
- www.bramblefordwinecellar.com.au
- bramblefordwinecellar@mailvista.com
- Additional icons: Searchly, Snapgram, Friendbook, Chatterly
4. Once again, forget it is a commercial card, make it special.

```html
<!DOCTYPE html>
<html lang="en">
<head>
<meta charset="utf-8">
<title>Brambleford Wine Cellar — Business Card</title>
<link rel="stylesheet" href="https://fonts.googleapis.com/css2?family=Cinzel:wght@400&family=Montserrat:wght@400;500&display=swap">
<style>
  :root {
    --stage: #2a2c30;
    --wine: #b81a45;
    --wine-deep: #9a1430;
    --wine-bright: #c72050;
    --paper: #ffffff;
    --ink-grey: #8a8a8a;
    --rule-grey: #d8d8d8;
    --blush: #f3e3e7;
  }
  * { margin: 0; padding: 0; box-sizing: border-box; }
  html, body { width: 1200px; height: 900px; overflow: hidden; }
  body {
    background: var(--stage);
    position: relative;
    font-family: "Montserrat", sans-serif;
  }
  .card {
    position: absolute;
    width: 540px;
    height: 310px;
    overflow: hidden;
    border-radius: 2px;
  }

  /* Front card */
  .card-front {
    left: 600px;
    top: 110px;
    background: linear-gradient(160deg, var(--wine-deep) 0%, var(--wine-bright) 60%, var(--wine) 100%);
  }
  .front-pattern {
    position: absolute;
    inset: 0;
    background: linear-gradient(200deg, rgba(255,255,255,0.06), rgba(0,0,0,0.06));
  }
  .front-wordmark {
    position: absolute;
    left: 250px;
    top: 108px;
    color: var(--paper);
    font-family: "Cinzel", serif;
    font-weight: 400;
    display: flex;
    align-items: center;
    gap: 10px;
  }
  .wordmark-dot {
    width: 30px; height: 30px;
    border-radius: 50%;
    background: var(--paper);
  }
  .wordmark-text { display: flex; flex-direction: column; line-height: 1; }
  .wordmark-name { font-size: 30px; letter-spacing: 1px; }
  .wordmark-sub { font-size: 12px; letter-spacing: 5px; margin-top: 6px; padding-left: 24px; }
  .front-rule {
    position: absolute;
    left: 96px; top: 158px;
    width: 130px; height: 1px;
    background: rgba(255,255,255,0.7);
  }
  .social-list {
    position: absolute;
    left: 70px; top: 172px;
    display: flex; gap: 10px;
    list-style: none;
  }
  .social-item {
    display: flex; flex-direction: column; align-items: center; gap: 3px;
    color: var(--paper);
    font-size: 7px;
    letter-spacing: 0.3px;
  }
  .social-dot {
    width: 18px; height: 18px;
    border-radius: 50%;
    background: var(--paper);
  }

  /* Back card */
  .card-back {
    left: 60px;
    top: 480px;
    background: var(--paper);
  }
  .back-band {
    position: absolute;
    left: 0; top: 0;
    width: 168px; height: 100%;
    background: linear-gradient(180deg, var(--wine-bright), var(--wine-deep));
    border-right: 6px solid var(--rule-grey);
  }
  .back-wordmark {
    position: absolute;
    left: 84px; top: 155px;
    transform: translate(-50%, -50%) rotate(-90deg);
    color: var(--paper);
    font-family: "Cinzel", serif;
    font-weight: 400;
    text-align: center;
    white-space: nowrap;
    line-height: 1;
  }
  .back-wordmark .wordmark-name { font-size: 28px; }
  .back-wordmark .wordmark-sub { font-size: 11px; padding-left: 0; margin-top: 6px; letter-spacing: 6px; }
  .back-emblem {
    position: absolute;
    right: 16px; bottom: 14px;
    width: 150px; height: 140px;
    border-radius: 50% 50% 40% 40%;
    background: var(--blush);
  }
  .back-content {
    position: absolute;
    left: 200px; top: 36px;
    right: 20px;
  }
  .person-name {
    font-family: "Cinzel", serif;
    color: var(--wine);
    font-size: 18px;
    letter-spacing: 0.5px;
  }
  .person-role {
    color: var(--ink-grey);
    font-size: 12px;
    margin-top: 2px;
  }
  .contact-list {
    list-style: none;
    margin-top: 22px;
    display: flex; flex-direction: column; gap: 5px;
  }
  .contact-item {
    display: flex; align-items: center; gap: 8px;
    color: var(--ink-grey);
    font-size: 11.5px;
  }
  .contact-icon { width: 12px; height: 12px; flex: none; }
  .address {
    margin-top: 26px;
    color: var(--ink-grey);
    font-size: 12px;
    line-height: 1.35;
    font-style: normal;
  }
</style>
</head>
<body>

<section class="card card-front" aria-label="Business card front">
  <div class="front-pattern" role="img" aria-label="Repeating tone-on-tone logo pattern"></div>
  <div class="front-wordmark">
    <span class="wordmark-dot"></span>
    <span class="wordmark-text">
      <span class="wordmark-name">BRAMBLEFORD</span>
      <span class="wordmark-sub">WINE CELLAR</span>
    </span>
  </div>
  <div class="front-rule"></div>
  <ul class="social-list">
    <li class="social-item"><span class="social-dot"></span>Chatterly</li>
    <li class="social-item"><span class="social-dot"></span>Searchly</li>
    <li class="social-item"><span class="social-dot"></span>Friendbook</li>
    <li class="social-item"><span class="social-dot"></span>Snapgram</li>
  </ul>
</section>

<section class="card card-back" aria-label="Business card back">
  <div class="back-band">
    <div class="back-wordmark">
      <div class="wordmark-name">BRAMBLEFORD</div>
      <div class="wordmark-sub">WINE CELLAR</div>
    </div>
  </div>
  <div class="back-emblem" role="img" aria-label="Faint large brand emblem"></div>
  <div class="back-content">
    <h1 class="person-name">MARLOW PRITCHARD</h1>
    <p class="person-role">Sales Manager</p>
    <ul class="contact-list">
      <li class="contact-item">
        <svg class="contact-icon" viewBox="0 0 12 12"><circle cx="6" cy="6" r="5.3" fill="none" stroke="#b81a45" stroke-width="1"/><path d="M4 3.2l1 1.3-.6.7c.4.9 1 1.5 1.9 1.9l.7-.6 1.3 1-.6 1c-2.2-.2-4.3-2.3-4.5-4.5z" fill="#b81a45"/></svg>
        +61 3 9018 4637
      </li>
      <li class="contact-item">
        <svg class="contact-icon" viewBox="0 0 12 12"><rect x="1" y="2.5" width="10" height="7" fill="none" stroke="#b81a45" stroke-width="1"/><path d="M1 2.5l5 4 5-4" fill="none" stroke="#b81a45" stroke-width="1"/></svg>
        bramblefordwinecellar@mailvista.com
      </li>
      <li class="contact-item">
        <svg class="contact-icon" viewBox="0 0 12 12"><circle cx="6" cy="6" r="5.3" fill="#b81a45"/><path d="M.8 6h10.4M6 .7c-2 2.9-2 7.7 0 10.6M6 .7c2 2.9 2 7.7 0 10.6" fill="none" stroke="#fff" stroke-width=".7"/></svg>
        www.bramblefordwinecellar.com.au
      </li>
    </ul>
    <address class="address">
      42 Ferncastle Steet<br>
      Alderbrook, Wynmoor<br>
      Australia 3999
    </address>
  </div>
</section>

</body>
</html>
```